ORBIT Learning League - Coalition for Fair Access in Digital Schooling - Sticker for Laptops, Branding

We need a sticker design for the ORBIT Learning League that we can share at our own events and at exhibitor booths at other events. We have a logo that you can incorporate, but we welcome creative designs. We want something colorful that will stand out - not just the existing logo on a plain white background! We are also including the PixelHive "add-on" project to design an updated/alternative logo/brand as an add-on!

About ORBIT:
Nationally, there are significant disparities in computer science (CS) degree programs and in the computing workforce with respect to race, gender, and intersections thereof. Only 21% of CS graduates identified as women, 3% as Black, and 8.5% as Hispanic. These trends continue in industry; only 24% of tech professionals identify as women, 3.1% as having a disability, 8.8% as Black, and 8% as Hispanic.

The ORBIT Learning League (www.orbitlearningleague.example) is a national alliance of colleges and universities, with a mission to shift practices in college computing departments to advance diversity, equity, and inclusion in computing. Specifically, ORBIT provides training, resources, and community to help college faculty and students to develop as leaders who take action to eliminate barriers to participation for historically excluded groups in computing and to advance diversity, equity, and inclusion in computing.

Typically, college students participating in a ORBIT Learning League chapter will work with K12 teachers in their local communities to provide or enhance learning opportunities for K12 students. These projects are designed to promote persistence and career advancement in computing, by connecting computing to community and societal impacts; reinforcing computing knowledge through teaching and practice; developing professional, entrepreneurial, and creative skills, and developing a network of computing professionals with a shared commitment to diversity, equity, and computing. Faculty participating in ORBIT will typically adopt an inclusive practice within their department and/or engage in research that advances justice-centered computing education and workforce preparation.

An analysis of over 10 years of surveys from more than 2000 ORBIT students (38% Black, 8.7% Hispanic, 28% White/Asian/Multiracial/Other Women, and 24% White/Asian Men) shows that students felt that the ORBIT increased their intentions to persist in computing. These results were significantly higher for Black women and Black men. In addition, ORBIT students had positive gains in GPA, self-efficacy, computing identity, and commitment to computing, with enhanced outcomes for students who identify as women, Black, Hispanic, Native American, and Pacific Islander/Native Hawaiian.

Target Market(s)

diversity in tech, college faculty in computer science, college students in computer science,

Industry/Entity Type

computer science, tech, higher education

Font styles to use
Sans Serif

Colors
0054AA
0677BA
7BADD7
CADEEF
E8F1F8
0094D4
00A9DD
6FCCEA
C7EBF8
E9F6FB
E54698
E96AAD
F1A4CE
F9D9EA
FCEFF6
A7469A
B969AE
D3A5CF
EDDBEB
F8F0F9
6B429C
8869AF
B7A5CE
E3DAEB
F3F0F8

```html
<!DOCTYPE html>
<html lang="en">
<head>
<meta charset="utf-8">
<title>ORBIT Learning League – Different But Equal Sticker</title>
<link href="https://fonts.googleapis.com/css2?family=Jost:wght@300;500;700&display=swap" rel="stylesheet">
<style>
  :root {
    --backdrop: #2b5088;
    --sticker: #050505;
    --ink-white: #f2f2f0;
    --navy: #0a36a3;
    --blue: #0054AA;
    --blue-mid: #0677BA;
    --cyan: #00A9DD;
    --sky: #0094D4;
    --pink: #E54698;
    --pink-light: #F1A4CE;
    --pink-pale: #F9D9EA;
    --purple: #6B429C;
    --violet: #8869AF;
  }
  html, body {
    margin: 0;
    width: 1200px;
    height: 911px;
    overflow: hidden;
    background: var(--backdrop);
  }
  .canvas { display: block; width: 1200px; height: 911px; }
  .sticker-disc { fill: var(--sticker); }
  .headline { font-family: "Jost", sans-serif; font-weight: 700; }
  .word-different { font-size: 62px; }
  .word-but { font-size: 176px; fill: var(--navy); }
  .word-equal { font-size: 78px; fill: var(--ink-white); }
  .chevron { fill: none; stroke-width: 15; stroke-linejoin: miter; stroke-linecap: butt; }
  .chevron-pink { stroke: var(--pink); }
  .chevron-pale { stroke: var(--pink-pale); }
  .chevron-cyan { stroke: var(--sky); }
  .chevron-purple { stroke: var(--violet); }
  .brand-dot { fill: var(--cyan); }
  .brand-name { font-family: "Jost", sans-serif; font-weight: 300; font-size: 23px; letter-spacing: 5px; fill: var(--ink-white); }
  .brand-url { font-family: "Jost", sans-serif; font-weight: 300; font-size: 9.5px; fill: var(--ink-white); }
</style>
</head>
<body>
<svg class="canvas" viewBox="0 0 1200 911" xmlns="http://www.w3.org/2000/svg" role="img" aria-label="Different but equal sticker for ORBIT Learning League">
  <circle class="sticker-disc" cx="594" cy="441" r="294"/>

  <polyline class="chevron chevron-pink" points="503,236 446,245 477,292"/>
  <polyline class="chevron chevron-pale" points="719,407 750,376 772,428"/>
  <polyline class="chevron chevron-cyan" points="384,530 392,590 446,555"/>
  <polyline class="chevron chevron-purple" points="731,562 770,604 714,612"/>

  <text class="headline word-different" x="441" y="343" textLength="292" lengthAdjust="spacingAndGlyphs"><tspan fill="var(--purple)">D</tspan><tspan fill="var(--cyan)">I</tspan><tspan fill="var(--pink)">F</tspan><tspan fill="var(--pink-light)">F</tspan><tspan fill="var(--blue)">E</tspan><tspan fill="var(--pink-light)">R</tspan><tspan fill="var(--pink-pale)">E</tspan><tspan fill="var(--blue-mid)">N</tspan><tspan fill="var(--pink)">T</tspan></text>

  <text class="headline word-but" x="441" y="487" textLength="292" lengthAdjust="spacingAndGlyphs">BUT</text>

  <text class="headline word-equal" x="436" y="561" textLength="306" lengthAdjust="spacingAndGlyphs">EQUAL.</text>

  <circle class="brand-dot" cx="597" cy="620" r="20"/>
  <text class="brand-name" x="597" y="689" text-anchor="middle">ORBIT</text>
  <text class="brand-url" x="597" y="703" text-anchor="middle">ORBITLEARNINGLEAGUE.EXAMPLE</text>
</svg>
</body>
</html>
```